Design A HVAC Business Website with Figma

We are launching a Web Design Service for HVAC and other Home Improvement businesses. We need to create some demo sites. These sites will be used to develop Webflow templates, so they must look very professional and real.

I am providing some sample data for this design. **,DO NOT USE LOREM IPSUM** anywhere in this design. We will be featuring these designs on our website and marketing materials.

More information can be found on this Notion page https://tidal-lantern-q41.pagevault-example.net/Site-Build-Brief-a3f9d27e81c04b5d96e1f0c7b2a48d13

Industry/Entity Type

HVAC, Plumbing, Remodeling, General Contractor

Number of Pages Required

5+ page

Requirements
Must have
• Must be professional

```html
<!DOCTYPE html>
<html lang="en">
<head>
<meta charset="utf-8">
<title>Keswick HVAC</title>
<link href="https://fonts.googleapis.com/css2?family=Poppins:wght@400;500;600;700&family=Raleway:wght@400;500;600&display=swap" rel="stylesheet">
<style>
:root{
  --black:#0b0b0b;
  --blue:#1466b8;
  --teal:#1a8fbf;
  --teal-btn:#1395c6;
  --ink:#333;
  --grey-bg:#f3f3f3;
  --guarantee-bg:#cfe9f0;
  --gallery-bg:#e6ecf1;
  --footer:#2b2b2b;
  --hero-dark:#2d3338;
  --white:#fff;
}
*{box-sizing:border-box;margin:0;padding:0}
html,body{width:1200px;height:3687px;overflow:hidden}
body{position:relative;background:var(--white);font-family:"Raleway",sans-serif;color:var(--ink)}
.abs{position:absolute}
.center{text-align:center;left:0;width:1200px}
a{color:inherit;text-decoration:none}

.top-nav{top:0;left:0;width:1200px;height:68px;background:var(--black);display:flex;align-items:center;justify-content:space-between;padding:0 113px;font-size:17px;color:#fff}

.site-header{top:68px;left:0;width:1200px;height:118px;background:#fff}
.brand{left:114px;top:36px;font-family:"Poppins",sans-serif;font-size:41px;font-weight:500;color:var(--teal);line-height:1}
.btn{position:absolute;display:flex;align-items:center;justify-content:center;border-radius:6px;font-family:"Poppins",sans-serif;font-weight:600;font-size:15px;color:#fff}
.btn-schedule{left:684px;top:36px;width:182px;height:52px;background:var(--teal-btn)}
.btn-finance{left:882px;top:36px;width:205px;height:52px;background:var(--blue)}

.hero{top:186px;left:0;width:1200px;height:558px;overflow:hidden;background:var(--hero-dark)}
.hero-photo{position:absolute;inset:0;
  background:
    linear-gradient(180deg,var(--hero-dark) 0%,rgba(45,51,56,.97) 40%,rgba(45,51,56,.55) 62%,rgba(45,51,56,.1) 85%,rgba(45,51,56,0) 100%),
    linear-gradient(90deg,#d9d6cf 0%,#a3998c 16%,#b84a3c 36%,#8d8f92 55%,#b8a070 68%,#7f8c99 80%,#c83a3a 92%,#9a9a9a 100%);}
.hero-copy{position:absolute;z-index:1;color:#fff}
.hero h1{top:62px;font-family:"Poppins",sans-serif;font-weight:600;font-size:29px;line-height:51px}
.hero p{top:178px;font-size:15.5px}
.hero .btn-outline{left:472px;top:226px;width:256px;height:52px;border:2px solid var(--teal-btn);border-radius:6px;display:flex;align-items:center;justify-content:center;font-family:"Poppins",sans-serif;font-weight:600;font-size:15px;background:rgba(45,51,56,.6)}

.section-title{font-family:"Poppins",sans-serif;font-weight:700;font-size:30px;color:var(--blue);line-height:1}
.about-title{left:113px;top:825px}
.about-text{left:113px;top:893px;width:443px;font-size:15px;line-height:30px;text-align:justify}
.btn-learn{left:113px;top:1133px;width:136px;height:51px;background:var(--blue)}
.about-frame{left:622px;top:829px;width:466px;height:362px;border:8px solid var(--teal-btn);background:#fff;padding:2px}
.about-frame div{width:100%;height:100%;background:linear-gradient(120deg,#e8ecef 0%,#3a6cc4 40%,#2b57a8 70%,#d4d8dc 100%)}

.services{top:1280px;left:0;width:1200px;height:834px;background:var(--grey-bg)}
.services-title{top:89px}
.tile{position:absolute;width:295px;height:258px;display:flex;align-items:center;justify-content:center;font-family:"Poppins",sans-serif;font-weight:700;font-size:29px;color:#fff;text-align:center}
.tile-heating{left:112px;top:183px;background:linear-gradient(135deg,#4a4a4a,#8a4a3e 60%,#555)}
.tile-cooling{left:452px;top:183px;background:linear-gradient(180deg,#19a0c6,#1791b8);font-family:"Raleway",sans-serif;font-weight:400;font-size:15.5px;line-height:26px;padding:0 28px}
.tile-plumbing{left:794px;top:183px;background:linear-gradient(135deg,#8a8478,#6a655c 60%,#a39a80)}
.tile-generators{left:112px;top:482px;background:linear-gradient(180deg,#8fa0b0,#c9cbcc 50%,#9a9d9e)}
.tile-fireplaces{left:452px;top:482px;background:linear-gradient(180deg,#2e2a26,#8a5a26 55%,#3a342e)}
.tile-air{left:794px;top:482px;background:linear-gradient(90deg,#c9ced2,#a9a8a6 60%,#7d6a5a)}

.guarantee-back{left:157px;top:2177px;width:917px;height:293px;background:var(--blue)}
.guarantee-box{left:126px;top:2209px;width:916px;height:294px;background:var(--guarantee-bg)}
.guarantee-title{top:2256px}
.guarantee-text{left:190px;top:2320px;width:820px;text-align:center;font-size:15px;line-height:30px}
.btn-guarantee{left:468px;top:2477px;width:264px;height:51px;background:var(--blue)}

.partners{top:2630px;left:0;width:1200px;height:70px}
.badge{position:absolute;top:0;height:64px;width:132px;background:#b9bcbf;border-radius:6px}

.gallery{top:2799px;left:0;width:1200px;height:522px;background:var(--gallery-bg)}
.gallery-title{top:72px}
.shot{position:absolute;top:164px;width:225px;height:272px}
.shot-filter{left:113px;background:linear-gradient(135deg,#d9dde0,#8c6b45 50%,#2b4f8a)}
.shot-tools{left:363px;background:linear-gradient(135deg,#c9ccd0,#8f9499 55%,#e3e4e5)}
.shot-unit{left:613px;background:linear-gradient(135deg,#2e2e2e,#efefef 50%,#c9302c)}
.shot-insulation{left:864px;background:linear-gradient(135deg,#caa45a,#e7c982 50%,#b8864a)}

.site-footer{top:3321px;left:0;width:1200px;height:366px;background:var(--footer);color:#fff}
.pill{position:absolute;top:91px;width:218px;height:35px;background:#fff;border-radius:18px;display:flex;align-items:center;justify-content:center;gap:8px;font-family:"Poppins",sans-serif;font-weight:700;font-size:17px;color:var(--blue)}
.footer-rule{position:absolute;left:127px;top:161px;width:950px;height:1px;background:#444}
.footer-phone{top:190px;font-family:"Poppins",sans-serif;font-size:30px;font-weight:500}
.footer-links{top:258px;display:flex;justify-content:center;gap:42px;font-size:15.5px}
.copyright{top:306px;font-size:15.5px}
</style>
</head>
<body>

<nav class="top-nav abs">
  <a>Home</a><a>Products &amp; Services</a><a>Reviews by City</a><a>About</a><a>Contact Us</a><a>Info</a><a>Gallery</a>
</nav>

<header class="site-header abs">
  <div class="brand abs">Keswick HVAC</div>
  <a class="btn btn-schedule">SCHEDULE SERVICE</a>
  <a class="btn btn-finance">APPLY FOR FINANCING</a>
</header>

<section class="hero abs">
  <div class="hero-photo" role="img" aria-label="Plumbing fittings, valves, pipes and wrenches laid out on a dark surface"></div>
  <h1 class="hero-copy center">EXPERT AC, HEAT PUMP, GENERATOR, GAS LOG &amp;<br>PLUMBING REPAIR AT EXCELLENT PRICES.</h1>
  <p class="hero-copy center">Briarwood Engineering Has Been Serving Anne Arundel County And Prince George's County Since 1962</p>
  <a class="btn-outline hero-copy">SCHEDULE AN APPOINTMENT</a>
</section>

<h2 class="section-title about-title abs">ABOUT KESWICK HVAC</h2>
<p class="about-text abs">We are insulation specialists with ample experience in both commercial and residential service. Our reputation is built on service, dependability, and customer satisfaction. We are fully licensed and insured in the state of Michigan and have over 14 years of experience in making buildings more efficient. Call us at +1 (555) 214 0376 to get a quote on insulation installation in Fort Gratiot, Port Huron, or Marysville.</p>
<a class="btn btn-learn">LEARN MORE</a>
<div class="about-frame abs"><div role="img" aria-label="Plumber in blue uniform repairing pipes under a sink"></div></div>

<section class="services abs">
  <h2 class="section-title services-title abs center">OUR SERVICES</h2>
  <div class="tile tile-heating" role="img" aria-label="Technician servicing a furnace">HEATING</div>
  <div class="tile tile-cooling">Looking For A Local Air Conditioning Company? You Can Count On The Hvac Experts At Briarwood To Handle Your Ac Repair Or Replacement.</div>
  <div class="tile tile-plumbing" role="img" aria-label="Plumber working on wall pipes">PLUMBING</div>
  <div class="tile tile-generators" role="img" aria-label="Standby generator unit outdoors">GENERATORS</div>
  <div class="tile tile-fireplaces" role="img" aria-label="Gas fireplace with glowing flames">FIREPLACES</div>
  <div class="tile tile-air" role="img" aria-label="Air purifier in a home with a phone app">AIR QUALITY</div>
</section>

<div class="guarantee-back abs"></div>
<div class="guarantee-box abs"></div>
<h2 class="section-title guarantee-title abs center">OUR GUARANTEE</h2>
<p class="guarantee-text abs">Harlow's Service, Inc. Guarantees That When The Equipment We Have Installed Is Maintained And Operated In Accordance With The Manufacturer's Operating And Maintenance Manuals, The System Will Perform As We Have Stated And Agreed Upon. If You Are Not Satisfied, We Will Make Any Necessary Modifications, Repairs, Or Replacements At No Charge To You For A Period Of 5 Years.</p>
<a class="btn btn-guarantee">SCHEDULE YOUR APPOINTMENT</a>

<div class="partners abs" aria-label="Partner and certification badges">
  <span class="badge" style="left:48px"></span>
  <span class="badge" style="left:210px"></span>
  <span class="badge" style="left:372px"></span>
  <span class="badge" style="left:534px"></span>
  <span class="badge" style="left:695px"></span>
  <span class="badge" style="left:858px"></span>
  <span class="badge" style="left:1021px"></span>
</div>

<section class="gallery abs">
  <h2 class="section-title gallery-title abs center">OUR GALLERY</h2>
  <div class="shot shot-filter" role="img" aria-label="Hand replacing a ceiling air filter"></div>
  <div class="shot shot-tools" role="img" aria-label="Plumbing tools laid beside a toilet"></div>
  <div class="shot shot-unit" role="img" aria-label="Technician installing an outdoor AC unit"></div>
  <div class="shot shot-insulation" role="img" aria-label="Fiberglass insulation rolls in an attic"></div>
</section>

<footer class="site-footer abs">
  <a class="pill" style="left:127px">GET SERVICE</a>
  <a class="pill" style="left:372px">EMAIL US</a>
  <a class="pill" style="left:616px">
    <svg width="18" height="18" viewBox="0 0 24 24"><path d="M12 2l3 7 7 .6-5.3 4.6 1.6 7.3L12 17.8 5.7 21.5l1.6-7.3L2 9.6 9 9z" fill="#f5a623"/></svg>
    EMPLOYMENT
    <svg width="18" height="18" viewBox="0 0 24 24"><path d="M12 2l3 7 7 .6-5.3 4.6 1.6 7.3L12 17.8 5.7 21.5l1.6-7.3L2 9.6 9 9z" fill="#f5a623"/></svg>
  </a>
  <a class="pill" style="left:860px">SPECIALS</a>
  <div class="footer-rule"></div>
  <div class="footer-phone abs center">+1 (555) 214 0376</div>
  <nav class="footer-links abs center">
    <a>Home</a><a>Products &amp; Services</a><a>Reviews by City</a><a>About</a><a>Contact Us</a><a>Info</a><a>Gallery</a>
  </nav>
  <div class="copyright abs center">©Copyrights 2023 Company Name &nbsp;|&nbsp; All Rights Reserved</div>
</footer>

</body>
</html>
```